Rugby Vanguards Rising Captains Scheme Website Design

Task:

A Website Design that has the ability for people to book onto events and Pay.

The design should reflect the colours and brand of the logo and what you have done for the Flyer, Facebook and Twitter pages. The same brand Family. The website needs to be clean and not cluttered.

5 Pages which include:

1. Home
2. Programme
3. Booking
4. FAQs
5. Vanguards

It should clean, easy to read and inviting for children to book onto the programme.

The Website domain will be www.vanguards-rcs.example

Happy to use rugby stock pictures children if you need to. Must be Rugby.

Target Market(s)

Children Age 11+ and their Parents

Contact Information for Business Card

One Side the Logo

Other side: Name. Job. Contact No. Email. Rising Captains Scheme

Number of Pages Required

5+ page

Font styles to use
Serif
Sans Serif

Requirements
Must have
• The flyer design attached as a document shows the colours of the brand - this MUST be consistent throughout the 5 Pages
• I must be able to use https://www.tixora.example for booking the events online
• The Business Card Files must allow me to change names, roles etc
Should not have
• It should not be cluttered

```html
<!DOCTYPE html>
<html lang="en">
<head>
<meta charset="utf-8">
<title>Rugby Vanguards Rising Captains Scheme</title>
<link rel="stylesheet" href="https://fonts.googleapis.com/css2?family=Oswald:wght@300;400;500&family=Open+Sans:wght@400;600;700&display=swap">
<style>
:root{
  --gold:#e3ac14;
  --gold-dark:#b8860b;
  --gold-light:#f2cf5a;
  --ink:#111111;
  --nav:#333333;
  --header-bg:#efefef;
  --cards-bg:#ececec;
  --white:#ffffff;
  --grey-text:#555555;
  --footer:#000000;
}
*{box-sizing:border-box;margin:0;padding:0}
html,body{width:1200px;height:2400px;overflow:hidden;background:var(--white)}
body{position:relative;font-family:"Open Sans",Arial,sans-serif;color:var(--ink)}
.abs{position:absolute}

/* header */
.site-header{left:0;top:0;width:1200px;height:180px;background:var(--header-bg)}
.brand{display:flex;flex-direction:column;align-items:center;gap:8px;width:150px}
.brand-mark{width:56px;height:56px;border-radius:50%;background:var(--gold)}
.brand-name{font-family:"Oswald",sans-serif;font-weight:500;font-size:18px;line-height:20px;color:var(--gold);text-align:center;text-transform:uppercase}
.header-brand{left:66px;top:26px}
.book-programme{left:574px;top:37px;width:540px;height:106px;background:linear-gradient(135deg,var(--gold-dark),var(--gold-light) 45%,var(--gold-dark));display:flex;align-items:center;justify-content:center}
.book-programme span{display:flex;align-items:center;justify-content:center;width:516px;height:84px;border:3px solid var(--white);font-family:"Oswald",sans-serif;font-weight:500;font-size:56px;letter-spacing:6px;color:var(--white)}

/* nav */
.main-nav{left:0;top:180px;width:1200px;height:63px;background:var(--nav)}
.nav-link{top:22px;font-size:15px;color:var(--white);text-transform:uppercase}
.nav-sep{top:20px;font-size:16px;color:var(--white)}
.social{display:flex;gap:11px}
.social-box{width:36px;height:36px;border:2px solid var(--white)}
.nav-social{left:984px;top:13px}

/* hero */
.hero{left:0;top:243px;width:1200px;height:637px;background:linear-gradient(100deg,#b59b78 0%,#8b7c66 25%,#2a4fb0 45%,#2451c4 70%,#3a5fc0 100%)}
.hero-panel{left:88px;top:337px;width:425px;height:442px;background:rgba(30,30,30,.72);border:3px solid var(--gold);padding:30px 16px 0 16px;color:var(--white)}
.hero-title{font-family:"Oswald",sans-serif;font-weight:400;font-size:34px;letter-spacing:3px;line-height:40px;white-space:nowrap}
.hero-text{margin-top:16px;font-size:15.5px;line-height:26px}
.btn{display:flex;align-items:center;justify-content:center;font-family:"Oswald",sans-serif;font-size:19px;color:var(--white);text-transform:uppercase}
.btn-gold{background:var(--gold);width:170px;height:59px;margin-top:22px;margin-left:2px}

/* event */
.event{left:0;top:880px;width:1200px;height:580px;background:linear-gradient(100deg,#d9dfe9 0%,#eef0ea 35%,#e7e9e4 60%,#e2e6ee 100%)}
.event-title{left:0;top:930px;width:1200px;text-align:center;font-family:"Oswald",sans-serif;font-weight:300;font-size:60px;letter-spacing:2px;line-height:80px}
.event-date{left:0;top:1026px;width:1200px;text-align:center;font-family:"Oswald",sans-serif;font-weight:500;font-size:16px;letter-spacing:1px}
.count-box{top:1115px;width:122px;height:165px;border:3px solid var(--ink);display:flex;flex-direction:column;align-items:center;justify-content:center;font-family:"Oswald",sans-serif;font-weight:500;line-height:1.05}
.count-num{font-size:58px}
.count-unit{font-size:40px}
.btn-black{left:515px;top:1332px;width:170px;height:61px;background:var(--ink)}

/* cards */
.cards{left:0;top:1460px;width:1200px;height:625px;background:var(--cards-bg)}
.card{top:1515px;width:331px;height:508px;background:var(--white);border:1px solid #d6d6d6}
.card-heading{position:absolute;left:19px;top:20px;font-size:17px;color:var(--grey-text);text-transform:uppercase}
.card-media{position:absolute;left:19px;top:60px;width:291px;height:380px}
.card-meta{position:absolute;left:19px;top:468px;display:flex;align-items:center;gap:8px;font-size:15px;color:var(--grey-text)}
.card-meta .divider{width:2px;height:24px;background:#888;margin:0 6px}
.card-go{position:absolute;right:18px;top:458px;width:52px;height:52px;border-radius:50%;background:var(--gold);color:var(--white);font-family:"Oswald",sans-serif;font-size:22px;display:flex;align-items:center;justify-content:center}

/* footer */
.site-footer{left:0;top:2085px;width:1200px;height:315px;background:var(--footer)}
.footer-link{top:2154px;font-size:13px;color:var(--white);text-transform:uppercase}
.footer-sep{top:2150px;font-size:16px;color:var(--white)}
.footer-brand{left:525px;top:2100px}
.footer-rule{top:2273px;height:1px;background:#555}
.footer-social{left:505px;top:2256px}
.footer-social .social-box{width:32px;height:32px;border-width:2px}
.copyright{left:0;top:2330px;width:1200px;text-align:center;font-size:12px;color:#8a8a8a}
</style>
</head>
<body>

<header class="site-header abs">
  <div class="brand header-brand abs">
    <div class="brand-mark"></div>
    <div class="brand-name">Rugby<br>Vanguards</div>
  </div>
  <a class="book-programme abs"><span>BOOK PROGRAMME</span></a>
</header>

<nav class="main-nav abs">
  <span class="nav-link abs" style="left:85px">Home</span>
  <span class="nav-sep abs" style="left:181px">|</span>
  <span class="nav-link abs" style="left:232px">Programme</span>
  <span class="nav-sep abs" style="left:381px">|</span>
  <span class="nav-link abs" style="left:434px">Booking</span>
  <span class="nav-sep abs" style="left:554px">|</span>
  <span class="nav-link abs" style="left:608px">FAQs</span>
  <span class="nav-sep abs" style="left:696px">|</span>
  <span class="nav-link abs" style="left:748px">Vanguards</span>
  <div class="social nav-social abs" aria-label="Social links">
    <span class="social-box"></span><span class="social-box"></span><span class="social-box"></span>
  </div>
</nav>

<section class="hero abs" role="img" aria-label="Photo of young rugby players in blue kit huddled together"></section>
<div class="hero-panel abs">
  <h1 class="hero-title">TRAIN, COMPETE, REPEAT</h1>
  <p class="hero-text">The Rising Captains Scheme is a Rugby Vanguards initiative. This is a fantastic opportunity to lead and play the Vanguards way. The programme is open to boys and girls from the areas of 11 upwards regardless of ability or skill level. We use Rugby as the vehicle to develop your leadership, communication and teamwork skills. If you are looking to have some fun and get that edge then this programme will be for you.</p>
  <a class="btn btn-gold">Book Now</a>
</div>

<section class="event abs" role="img" aria-label="Faded photo of children playing tag rugby in blue and yellow bibs"></section>
<h2 class="event-title abs">NEXT EVENT 2018</h2>
<p class="event-date abs">TUESDAY, JULY 15, 2018. HARBOUR PLAZA – EASTBROOK CITY</p>
<div class="count-box abs" style="left:85px"><span class="count-num">07</span><span class="count-unit">DAYS</span></div>
<div class="count-box abs" style="left:389px"><span class="count-num">04</span><span class="count-unit">HRS</span></div>
<div class="count-box abs" style="left:690px"><span class="count-num">42</span><span class="count-unit">MINS</span></div>
<div class="count-box abs" style="left:993px"><span class="count-num">00</span><span class="count-unit">SEC</span></div>
<a class="btn btn-black abs">Book Now</a>

<section class="cards abs"></section>

<article class="card abs" style="left:85px">
  <h3 class="card-heading">Heading Title Here</h3>
  <div class="card-media" role="img" aria-label="Photo of a child's hands holding a ball on grass" style="background:linear-gradient(180deg,#b8402f 0%,#6b4a35 45%,#5f7d3e 100%)"></div>
  <div class="card-meta">
    <svg width="16" height="16" viewBox="0 0 16 16"><rect x="1.5" y="3" width="13" height="11.5" fill="none" stroke="#555" stroke-width="1.6"/><line x1="1.5" y1="6.5" x2="14.5" y2="6.5" stroke="#555" stroke-width="1.6"/><line x1="5" y1="1" x2="5" y2="4" stroke="#555" stroke-width="1.6"/><line x1="11" y1="1" x2="11" y2="4" stroke="#555" stroke-width="1.6"/></svg>
    <span>11/03/17</span><span class="divider"></span>
    <svg width="18" height="18" viewBox="0 0 18 18"><circle cx="9" cy="9" r="7.5" fill="none" stroke="#555" stroke-width="1.6"/><path d="M9 4.5V9l3 2" fill="none" stroke="#555" stroke-width="1.6"/></svg>
    <span>10.00 AM</span>
  </div>
  <span class="card-go">GO</span>
</article>

<article class="card abs" style="left:434px">
  <h3 class="card-heading">Heading Title Here</h3>
  <div class="card-media" role="img" aria-label="Photo of a coach and young player holding a ball on a dark background" style="background:linear-gradient(135deg,#2a2a2a 0%,#5a4030 50%,#1a1a1a 100%)"></div>
  <div class="card-meta">
    <svg width="16" height="16" viewBox="0 0 16 16"><rect x="1.5" y="3" width="13" height="11.5" fill="none" stroke="#555" stroke-width="1.6"/><line x1="1.5" y1="6.5" x2="14.5" y2="6.5" stroke="#555" stroke-width="1.6"/><line x1="5" y1="1" x2="5" y2="4" stroke="#555" stroke-width="1.6"/><line x1="11" y1="1" x2="11" y2="4" stroke="#555" stroke-width="1.6"/></svg>
    <span>11/03/17</span><span class="divider"></span>
    <svg width="18" height="18" viewBox="0 0 18 18"><circle cx="9" cy="9" r="7.5" fill="none" stroke="#555" stroke-width="1.6"/><path d="M9 4.5V9l3 2" fill="none" stroke="#555" stroke-width="1.6"/></svg>
    <span>10.00 AM</span>
  </div>
  <span class="card-go">GO</span>
</article>

<article class="card abs" style="left:784px">
  <h3 class="card-heading">Heading Title Here</h3>
  <div class="card-media" role="img" aria-label="Photo of a young player in a helmet and red and black kit" style="background:linear-gradient(180deg,#3c3f42 0%,#2a2a2c 40%,#5a1e22 70%,#1e1e20 100%)"></div>
  <div class="card-meta">
    <svg width="16" height="16" viewBox="0 0 16 16"><rect x="1.5" y="3" width="13" height="11.5" fill="none" stroke="#555" stroke-width="1.6"/><line x1="1.5" y1="6.5" x2="14.5" y2="6.5" stroke="#555" stroke-width="1.6"/><line x1="5" y1="1" x2="5" y2="4" stroke="#555" stroke-width="1.6"/><line x1="11" y1="1" x2="11" y2="4" stroke="#555" stroke-width="1.6"/></svg>
    <span>11/03/17</span><span class="divider"></span>
    <svg width="18" height="18" viewBox="0 0 18 18"><circle cx="9" cy="9" r="7.5" fill="none" stroke="#555" stroke-width="1.6"/><path d="M9 4.5V9l3 2" fill="none" stroke="#555" stroke-width="1.6"/></svg>
    <span>10.00 AM</span>
  </div>
  <span class="card-go">GO</span>
</article>

<footer class="site-footer abs"></footer>
<span class="footer-link abs" style="left:110px">Home</span>
<span class="footer-sep abs" style="left:225px">|</span>
<span class="footer-link abs" style="left:306px">Programme</span>
<span class="footer-link abs" style="left:826px">Booking</span>
<span class="footer-sep abs" style="left:961px">|</span>
<span class="footer-link abs" style="left:1040px">FAQs</span>
<div class="brand footer-brand abs">
  <div class="brand-mark"></div>
  <div class="brand-name">Rugby<br>Vanguards</div>
</div>
<div class="footer-rule abs" style="left:85px;width:400px"></div>
<div class="footer-rule abs" style="left:715px;width:400px"></div>
<div class="social footer-social abs" aria-label="Social links">
  <span class="social-box"></span><span class="social-box"></span><span class="social-box"></span><span class="social-box"></span>
</div>
<p class="copyright abs">COPYRIGHT © 2018 VANGUARDS-RCS</p>

</body>
</html>
```